Halt and Thicken New Branding Stationary Set - updated Oct 30th 2017

Updated on 30th Oct 2017 as we now need a whole folder design instead of a folder cover. We have thought out exactly what should be on it so it wont be hard. We are happy for this to be completed only by the winning designer if you like. And also we are guaranteeing this project now. Thanks!

We just got our new logo and now we would like a stationary set so we can brand our company communications. The items we need designed are:
Business cards
Letterhead
Appointment confirmation cards
Folder - switched from folder cover. Note that if you don't wish to do this unless you are selected as the winner this is fine.

1. Business cards - for 5 employees, final names will be given once the winner is selected, but you can use this one as the sample:
Lucinda Prieto
Hair Regrowth Expert
Halt and Thicken
7127 Marbury Ave, Suite 500
Kestrel Park CA 90877
lucinda@gavinthorpemd.example
(555) 238-9016

2. Letterhead 8.5" x 11.0" vertical
Halt and Thicken
Kestrel Park CA 90877
office@haltandthicken.example
(555) 238-9016

3. Appointment Confirmation cards - business card size
Halt and Thicken
Kestrel Park CA 90877
Appointment For:
Date:
Time:
If you are unable to make your appointment, please contact us to reschedule at:
(555) 238-9016
info@gavinthorpemd.example

*UPDATED*
4. Folder 9" x 12 " vertical with double pocket
We would like the infinity image from the logo made really big so the left side is on the back and the right side with the + sign is on the front and its takes up the maximum room on the folder.
On the front below the half logo it should say "A Biochemical Revolution..."
On the inside we would also like to have the infinity sign from the logo but faded and half on the left pocket half on the right.
On left inside pocket it should say (this will be partically written on top of the logo):
Gavin Thorpe MD
Precision Medicine
Halt and Thicken Hair
On the Right inside pocket it should say the following:
Because the Enemy of BETTER Health is Good Health
BETTER Ingredients
BETTER Recipe
BETTER Medicine
On the back below the logo on the bottom should be the contact information.
I attached a picture of our drawing of what we want for this to make it easier.

Here is our website to give you an idea of our branding: http://www.haltandthicken.example/

We are the only true cure for hair loss and need to look professional and highest quality and beyond reproach from an ethical standpoint. We are a medical clinic so this should be portrayed also.
We cured hair loss by analyzing biochemistry and rebalancing it so that the process reverses and your own hair can grow back naturally.

Business card information:

OK so here is the information for the business cards:

Lucinda Prieto
Hair Regrowth Expert
(555) 238-9016
www.haltandthicken.example

Marisol Quintero
Hair Growth Consultant
(555) 238-9016
marisol@gavinthorpemd.example
www.haltandthicken.example

Glenda Hutchins
CMO/COO
(555) 238-9016
glenda@haltandthicken.example
www.haltandthicken.example

Dr Lou Thorpe
President
(555) 238-9016
info@gavinthorpemd.example
www.haltandthicken.example

Halt and Thicken
Customer Service
(555) 238-9016
info@gavinthorpemd.example
www.haltandthicken.example

Target Market(s)

Men aged 20-24 who care about their appearance, care about their hair and care about the world.

Industry/Entity Type

Medical And Science

Font styles to use
Sans Serif

Colors
00a990
ffffff
9d9d9d
333333

Requirements
Must have
• Must use the logo and our brand colors from the logo in all designs.
• The pantone colors are:
• Green: #4ca26f
• Light Grey: #999999
• The design should be symmetrical and balanced.
Nice to have
• It should look reasonably masculine.
Should not have
• Do not include any red in the design.

```html
<!DOCTYPE html>
<html lang="en">
<head>
<meta charset="utf-8">
<title>Halt and Thicken – Stationery Set</title>
<link rel="stylesheet" href="https://fonts.googleapis.com/css2?family=Open+Sans:wght@400;600;700&display=swap">
<style>
  :root {
    --green: #4ca26f;
    --grey: #999999;
    --grey-band: #707070;
    --ink: #555555;
    --ink-dark: #444444;
    --dark-card: #383636;
    --paper: #ffffff;
    --backdrop: #d2d2d2;
  }
  * { box-sizing: border-box; margin: 0; padding: 0; }
  html, body { width: 1200px; height: 904px; overflow: hidden; }
  body {
    background: var(--backdrop);
    font-family: "Open Sans", Arial, sans-serif;
    color: var(--ink);
    position: relative;
  }
  .piece { position: absolute; background: var(--paper); overflow: hidden; }
  .card { border-radius: 8px; }
  .card--dark { background: var(--dark-card); display: flex; align-items: center; justify-content: center; }
  .wordmark { color: var(--green); font-weight: 600; white-space: nowrap; line-height: 1; }
  .band { position: absolute; left: 0; right: 0; bottom: 0; display: flex; }
  .band__grey { background: var(--grey-band); }
  .band__green { background: var(--green); flex: 1; }
  .icon { width: 8px; height: 8px; flex: none; }
  .contact-line { display: flex; align-items: center; gap: 5px; white-space: nowrap; }

  /* Letterhead */
  .letterhead { left: 318px; top: 87px; width: 547px; height: 775px; }
  .letterhead .wordmark { position: absolute; left: 45px; top: 72px; font-size: 17px; }
  .letterhead__header { position: absolute; right: 30px; top: 79px; display: flex; font-size: 8.5px; line-height: 11.4px; white-space: nowrap; }
  .letterhead__address { padding-right: 6px; border-right: 1px solid var(--ink); }
  .letterhead__address strong { font-weight: 700; color: var(--ink-dark); }
  .letterhead__contacts { padding-left: 9px; }
  .letterhead .band { height: 15px; }
  .letterhead .band__grey { width: 273px; }

  /* Dark logo cards */
  .card-front--left { left: 53px; top: 285px; width: 233px; height: 134px; }
  .card-front--right { left: 906px; top: 434px; width: 232px; height: 135px; }
  .card--dark .wordmark { font-size: 19px; }

  /* Business card */
  .business-card { left: 53px; top: 438px; width: 233px; height: 133px; text-align: center; }
  .business-card .wordmark { position: absolute; left: 0; right: 0; top: 26px; font-size: 13px; }
  .business-card__name { position: absolute; left: 0; right: 0; top: 65px; font-size: 7.5px; font-weight: 700; color: var(--green); }
  .business-card__title { position: absolute; left: 0; right: 0; top: 76px; font-size: 6px; }
  .business-card__details { position: absolute; left: 0; right: 0; top: 94px; display: flex; justify-content: center; font-size: 6px; line-height: 9px; text-align: left; white-space: nowrap; }
  .business-card__address { text-align: right; padding-right: 4px; border-right: 1px solid var(--ink); }
  .business-card__address strong { color: var(--ink-dark); font-weight: 700; }
  .business-card__contacts { padding-left: 4px; }
  .business-card__contacts .icon { width: 6px; height: 6px; }
  .business-card .band { height: 6px; }
  .business-card .band__grey { width: 113px; }

  /* Appointment card */
  .appointment-card { left: 906px; top: 285px; width: 232px; height: 132px; }
  .appointment-card__heading { position: absolute; left: 16px; top: 13px; font-size: 7.5px; font-weight: 700; color: var(--ink-dark); }
  .appointment-card__fields { position: absolute; left: 16px; right: 15px; top: 30px; display: flex; align-items: flex-end; font-size: 7px; gap: 3px; white-space: nowrap; }
  .appointment-card__blank { border-bottom: 1px solid var(--grey); height: 8px; }
  .appointment-card__rule { position: absolute; left: 18px; right: 16px; top: 52px; border-top: 1px solid var(--grey); }
  .appointment-card__info { position: absolute; left: 0; right: 0; top: 67px; text-align: center; font-size: 6px; line-height: 8.8px; white-space: nowrap; }
  .appointment-card__info strong { color: var(--ink-dark); font-weight: 700; }
  .appointment-card__note { color: var(--green); }
  .appointment-card__info .contact-line { justify-content: center; gap: 3px; }
  .appointment-card__info .icon { width: 6px; height: 6px; }
  .appointment-card .band { height: 5px; }
  .appointment-card .band__grey { width: 116px; }
</style>
</head>
<body>
  <svg width="0" height="0" style="position:absolute" aria-hidden="true">
    <defs>
      <symbol id="icon-phone" viewBox="0 0 10 10"><path d="M2.2 0.8 L3.6 2.6 L2.8 3.6 C3.4 4.9 4.9 6.4 6.3 7.1 L7.3 6.3 L9.2 7.7 L8.2 9.2 C4.5 9 0.9 5.4 0.8 1.8 Z" fill="#4ca26f"/></symbol>
      <symbol id="icon-mail" viewBox="0 0 10 10"><rect x="0.8" y="2.2" width="8.4" height="6" rx="0.6" fill="#4ca26f"/><path d="M1.2 2.6 L5 5.6 L8.8 2.6" stroke="#fff" stroke-width="0.9" fill="none"/></symbol>
      <symbol id="icon-globe" viewBox="0 0 10 10"><circle cx="5" cy="5" r="4.2" fill="none" stroke="#4ca26f" stroke-width="1"/><ellipse cx="5" cy="5" rx="1.8" ry="4.2" fill="none" stroke="#4ca26f" stroke-width="0.8"/><line x1="0.8" y1="5" x2="9.2" y2="5" stroke="#4ca26f" stroke-width="0.8"/></symbol>
    </defs>
  </svg>

  <!-- Business card front, dark -->
  <section class="piece card card--dark card-front--left">
    <span class="wordmark">Halt and Thicken</span>
  </section>

  <!-- Business card back -->
  <section class="piece card business-card">
    <span class="wordmark">Halt and Thicken</span>
    <p class="business-card__name">Lucinda Prieto</p>
    <p class="business-card__title">Hair Regrowth Expert</p>
    <div class="business-card__details">
      <div class="business-card__address">
        <strong>Halt and Thicken</strong><br>
        7127 Marbury Ave, Suite 500<br>
        Kestrel Park CA 90877
      </div>
      <div class="business-card__contacts">
        <div class="contact-line"><svg class="icon"><use href="#icon-phone"/></svg>(555) 238-9016</div>
        <div class="contact-line"><svg class="icon"><use href="#icon-mail"/></svg>lucinda@gavinthorpemd.example</div>
        <div class="contact-line"><svg class="icon"><use href="#icon-globe"/></svg>www.gavinthorpemd.example</div>
      </div>
    </div>
    <div class="band"><span class="band__grey"></span><span class="band__green"></span></div>
  </section>

  <!-- Letterhead -->
  <section class="piece letterhead">
    <span class="wordmark">Halt and Thicken</span>
    <div class="letterhead__header">
      <div class="letterhead__address">
        <strong>Halt and Thicken</strong><br>
        7127 Marbury Ave, Suite 500<br>
        Kestrel Park CA 90877
      </div>
      <div class="letterhead__contacts">
        <div class="contact-line"><svg class="icon"><use href="#icon-phone"/></svg>(555) 238-9016</div>
        <div class="contact-line"><svg class="icon"><use href="#icon-mail"/></svg>office@gavinthorpemd.example</div>
        <div class="contact-line"><svg class="icon"><use href="#icon-globe"/></svg>www.gavinthorpemd.example</div>
      </div>
    </div>
    <div class="band"><span class="band__grey"></span><span class="band__green"></span></div>
  </section>

  <!-- Appointment card -->
  <section class="piece card appointment-card">
    <p class="appointment-card__heading">Appointment For:</p>
    <div class="appointment-card__fields">
      <span>Date:</span><span class="appointment-card__blank" style="width:96px"></span>
      <span style="margin-left:2px">Time:</span><span class="appointment-card__blank" style="width:42px"></span>
      <span>am/pm</span>
    </div>
    <div class="appointment-card__rule"></div>
    <div class="appointment-card__info">
      <strong>Halt and Thicken</strong><br>
      7127 Marbury Ave, Suite 500, Kestrel Park CA 90877<br>
      <span class="appointment-card__note">If you are unable to make your appointment<br>please contact us to reschedule at:</span>
      <div class="contact-line"><svg class="icon"><use href="#icon-phone"/></svg>(555) 238-9016</div>
      <div class="contact-line"><svg class="icon"><use href="#icon-mail"/></svg>info@gavinthorpemd.example</div>
    </div>
    <div class="band"><span class="band__grey"></span><span class="band__green"></span></div>
  </section>

  <!-- Appointment card front, dark -->
  <section class="piece card card--dark card-front--right">
    <span class="wordmark">Halt and Thicken</span>
  </section>
</body>
</html>
```